design a web site for equipment and software pos company

We would a web site similar to the site we whited labed our rtil system .https://tryplimvo.com/
website would be on RkTillDepot.com
we would a contact page
877-555-0142

We do not want an exact copy just something similar .
we are tablet po system

we are at

we are selling hardware and software

rk till depot
41 fernhollow ln
warren, nj 07318
we are cloud based system

Target Market(s)

any retail merchant

Industry/Entity Type

credit card processing in POS asystems

Coding

Coded - Design and coding required

Number of Pages Required

5+ page

Requirements
Must have
• be able to connect hostwren hosting
Nice to have
• modern looking site
Should not have
• any red

```html
<!DOCTYPE html>
<html lang="en">
<head>
<meta charset="utf-8">
<title>RK Till Depot — The Best POS System for Your Business</title>
<link href="https://fonts.googleapis.com/css2?family=Archivo+Black&family=Roboto:wght@300;400;500;700;900&family=Roboto+Condensed:wght@300;400;700&display=swap" rel="stylesheet">
<style>
:root{
  --yellow:#f1c40f;
  --yellow-soft:#f7e7a6;
  --ink:#1b1b1b;
  --dark:#222222;
  --text:#333333;
  --muted:#666666;
  --line:#cfcfcf;
  --white:#ffffff;
}
*{margin:0;padding:0;box-sizing:border-box}
html,body{width:1200px;height:3645px;overflow:hidden}
body{position:relative;font-family:'Roboto',sans-serif;color:var(--text);background:var(--white)}

/* header */
.site-header{position:absolute;left:0;top:0;width:1200px;height:68px;background:var(--ink)}
.brand{position:absolute;display:flex;align-items:center;gap:10px;color:var(--white);font-family:'Roboto Condensed',sans-serif;font-weight:400;white-space:nowrap}
.brand .mark{width:14px;height:14px;background:var(--yellow)}
.site-header .brand{left:172px;top:14px;font-size:30px}
.main-nav{position:absolute;left:477px;top:28px;display:flex;gap:15px;font-size:10px;color:var(--white);letter-spacing:.2px;white-space:nowrap}
.btn-proposal{position:absolute;left:911px;top:15px;width:127px;height:38px;border-radius:19px;background:var(--yellow);color:var(--ink);font-size:11px;display:flex;align-items:center;justify-content:center;gap:5px;white-space:nowrap}

/* hero */
.hero{position:absolute;left:0;top:68px;width:1200px;height:580px;overflow:hidden}
.hero-photo{position:absolute;inset:0;background:linear-gradient(110deg,#3a2e22 0%,#5b4a38 35%,#7b6b5c 60%,#3b3029 100%)}
.hero-badge{position:absolute;left:141px;top:95px;width:305px;height:305px;border-radius:50%;background:var(--yellow);text-align:center;padding-top:87px;color:var(--ink)}
.hero-badge .l1{font-size:34px;font-weight:300;letter-spacing:1px}
.hero-badge .l2{font-family:'Archivo Black',sans-serif;font-size:40px;line-height:1.05;white-space:nowrap}
.hero-badge .l3{font-size:28px;font-weight:300;white-space:nowrap}
.hero-curve{position:absolute;left:0;bottom:0}

/* welcome */
.welcome-title{position:absolute;left:0;top:690px;width:1200px;text-align:center;font-family:'Archivo Black',sans-serif;font-size:100px;color:var(--ink);text-shadow:4px 4px 0 var(--yellow);letter-spacing:-2px}
.ring{position:absolute;left:976px;top:743px;width:198px;height:198px;border-radius:50%;border:24px solid var(--yellow-soft)}
.welcome-copy{position:absolute;left:139px;top:832px;width:407px;font-size:10.6px;line-height:16.5px;text-align:justify;color:var(--text)}
.welcome-copy p+p{margin-top:14px}
.btn-contact{position:absolute;left:141px;top:1101px;width:210px;height:55px;background:var(--ink);border-left:6px solid var(--yellow);color:var(--white);font-family:'Roboto Condensed',sans-serif;font-weight:700;font-size:17px;display:flex;align-items:center;justify-content:center;gap:8px}
.laptop{position:absolute;left:495px;top:835px;width:691px;height:370px}
.laptop-screen{position:absolute;left:96px;top:0;width:500px;height:340px;border-radius:14px 14px 0 0;background:linear-gradient(180deg,#d8dadc,#eef2f4 40%,#cfd3d6)}
.laptop-base{position:absolute;left:0;top:340px;width:691px;height:18px;border-radius:0 0 40px 40px;background:linear-gradient(180deg,#d4d6d8,#9ea2a6)}

/* cloud */
.cloud-photo{position:absolute;left:0;top:1242px;width:569px;height:368px;background:linear-gradient(135deg,#5d646b,#9aa0a5 55%,#c9c4bd)}
.cloud-panel{position:absolute;left:579px;top:1242px;width:621px;height:368px;background:var(--yellow);padding:32px 170px 0 42px;color:var(--ink)}
.cloud-panel h2{font-family:'Roboto Condensed',sans-serif;font-weight:700;font-size:34px;letter-spacing:-.5px;white-space:nowrap}
.cloud-panel .dots{display:flex;gap:4px;margin:2px 0 10px}
.cloud-panel .dots i{width:5px;height:5px;border-radius:50%;background:var(--ink)}
.cloud-panel p{width:409px;font-size:10.6px;line-height:15px;text-align:justify;margin-bottom:12px}
.btn-outline{position:absolute;left:46px;top:296px;width:149px;height:37px;border:2px solid var(--ink);border-radius:19px;display:flex;align-items:center;justify-content:center;gap:5px;font-size:12px;font-weight:700}

/* pos features */
.pos{position:absolute;left:0;top:1612px;width:1200px;height:857px;background:linear-gradient(180deg,#e9e9e9,#f7f7f7 30%,#fafafa 70%,#eeeeee)}
.pos-title{position:absolute;left:0;top:30px;width:1200px;text-align:center;font-family:'Archivo Black',sans-serif;font-size:96px;color:var(--ink);text-shadow:4px 4px 0 var(--yellow)}
.pos-sub{position:absolute;left:0;top:145px;width:1200px;text-align:center;font-size:13.5px;color:var(--text)}
.orbit{position:absolute;left:0;top:0}
.feature{position:absolute;width:106px;height:106px;border-radius:50%;background:var(--yellow);display:flex;align-items:center;justify-content:center}
.feature-label{position:absolute;font-size:13px;color:var(--text);white-space:nowrap}
.hardware{position:absolute;left:382px;top:369px;width:389px;height:240px;border-radius:6px;background:linear-gradient(180deg,#d9dde0,#9aa0a4 60%,#5c6064)}

/* banner */
.banner{position:absolute;left:0;top:2469px;width:1200px;height:128px;background:var(--ink)}
.banner .brand{left:124px;top:40px;font-size:40px}
.banner .divider{position:absolute;left:371px;top:30px;width:1px;height:68px;background:#555}
.banner h3{position:absolute;left:396px;top:44px;font-family:'Roboto Condensed',sans-serif;font-weight:400;font-size:26px;line-height:30px;color:var(--white);letter-spacing:-.6px;white-space:nowrap}
.banner p{position:absolute;left:397px;top:80px;font-size:15px;font-weight:300;color:var(--white);white-space:nowrap}
.btn-banner{position:absolute;left:876px;top:50px;width:147px;height:38px;border:2px solid var(--white);border-radius:19px;color:var(--white);font-size:12px;font-weight:700;display:flex;align-items:center;justify-content:center;gap:5px}

/* business types */
.smart-title{position:absolute;left:0;top:2632px;width:1200px;text-align:center;font-family:'Roboto Condensed',sans-serif;font-weight:700;font-size:44px;color:var(--ink);letter-spacing:-.5px}
.smart-sub{position:absolute;left:0;top:2683px;width:1200px;text-align:center;font-size:27px;font-weight:300;letter-spacing:3px;color:var(--text)}
.hex{position:absolute;width:174px;height:198px;clip-path:polygon(50% 0,100% 25%,100% 75%,50% 100%,0 75%,0 25%);background:var(--yellow);display:flex;flex-direction:column;align-items:center;justify-content:center;gap:8px;color:var(--ink);font-size:14px;font-weight:500}

/* partners */
.partners-title{position:absolute;left:0;top:3172px;width:1200px;text-align:center;font-size:33px;font-weight:300;color:var(--text)}
.partner{position:absolute;top:3240px;width:158px;height:88px;border:1px solid var(--line);background:var(--white);display:flex;align-items:center;justify-content:center;gap:7px;font-family:'Roboto Condensed',sans-serif;font-weight:700;font-size:15px;color:#555}
.partner i{width:12px;height:12px;background:#777;display:block}
.arrow{position:absolute;top:3267px;width:32px;height:32px;background:#555;transform:rotate(45deg);display:flex;align-items:center;justify-content:center}

/* footer */
.site-footer{position:absolute;left:0;top:3360px;width:1200px;height:237px;background:var(--dark);color:var(--white)}
.foot-col{position:absolute;top:36px}
.foot-col h4{font-family:'Roboto Condensed',sans-serif;font-weight:700;font-size:17px;padding-bottom:8px;border-bottom:1px solid #555;margin-bottom:14px;min-width:135px;white-space:nowrap}
.foot-col ul{list-style:none;font-size:10px;line-height:21px;letter-spacing:.3px;white-space:nowrap}
.foot-col li::before{content:"›";margin-right:5px}
.news-input{position:absolute;width:244px;height:31px;border:1px solid #888;font-size:10.5px;color:#ccc;padding:9px 11px}
.btn-subscribe{position:absolute;left:782px;top:208px;width:102px;height:29px;background:var(--yellow);color:var(--ink);font-weight:700;font-size:13px;display:flex;align-items:center;justify-content:center}
.copyright{position:absolute;left:0;top:3597px;width:1200px;height:48px;background:var(--yellow);color:var(--ink);font-size:11.5px}
.copyright span{position:absolute;left:150px;top:17px}
.social{position:absolute;left:928px;top:17px;display:flex;gap:5px}
.social i{width:15px;height:15px;background:var(--ink);border-radius:2px;display:block}
</style>
</head>
<body>

<header class="site-header">
  <div class="brand"><span class="mark"></span>RK Till Depot</div>
  <nav class="main-nav"><span>HOME</span><span>ABOUT</span><span>BUSINESS TYPES</span><span>PRODUCTS</span><span>PARTNERS</span><span>WHITE LABEL</span></nav>
  <div class="btn-proposal">
    <svg width="11" height="11" viewBox="0 0 12 12"><rect x="1" y="1" width="10" height="10" rx="2" fill="none" stroke="#1b1b1b" stroke-width="1.4"/><path d="M4 8l4-4" stroke="#1b1b1b" stroke-width="1.4"/></svg>GET PROPOSAL
  </div>
</header>

<section class="hero">
  <div class="hero-photo" role="img" aria-label="Photo of a smiling cashier tapping a POS touchscreen in a shop"></div>
  <div class="hero-badge"><div class="l1">THE BEST</div><div class="l2">POS SYSTEM</div><div class="l3">FOR YOUR BUSINESS</div></div>
  <svg class="hero-curve" width="1200" height="200" viewBox="0 0 1200 200">
    <path d="M0 120 Q300 165 580 200 L620 200 Q950 140 1200 40 L1200 200 L0 200Z" fill="#f1c40f"/>
    <path d="M0 130 Q300 175 600 200 L0 200Z M600 200 Q900 160 1200 90 L1200 200Z" fill="#ffffff"/>
  </svg>
</section>

<h1 class="welcome-title">WELCOME</h1>
<div class="ring"></div>
<div class="welcome-copy">
  <p>Lorem Ipsum is simply dummy text of the printing and typesetting industry. Lorem Ipsum has been the industry's standard dummy text ever since the 1500s, when an unknown printer took a galley of type and scrambled it to make a type specimen book. It has survived not only five centuries. Lorem Ipsum is simply dummy text of the printing and typesetting industry. Lorem Ipsum has been the industry's standard dummy text ever since the 1500s, Lorem Ipsum has been the industry's standard dummy text ever since the 1500s,</p>
  <p>Lorem Ipsum is simply dummy text of the printing and typesetting industry. Lorem Ipsum has been the industry's standard dummy text ever since the 1500s, when an unknown printer took a galley of type and scrambled it to make a type specimen book. It has survived not only five centuries. Lorem Ipsum is simply dummy text of the printing and typesetting industry. Lorem Ipsum has been the industry's standard dummy text ever since the 1500s, Lorem Ipsum has been the industry's standard dummy text ever since the 1500s,</p>
</div>
<div class="btn-contact">
  <svg width="17" height="13" viewBox="0 0 17 13"><rect x="1" y="1" width="15" height="11" fill="none" stroke="#fff" stroke-width="1.6"/><path d="M1 1l7.5 6L16 1" fill="none" stroke="#fff" stroke-width="1.6"/></svg>CONTACT US
</div>
<div class="laptop" role="img" aria-label="Laptop showing the POS register screen with product grid and sale total">
  <div class="laptop-screen"></div>
  <div class="laptop-base"></div>
</div>

<div class="cloud-photo" role="img" aria-label="Photo of a hand using a countertop POS touchscreen terminal"></div>
<section class="cloud-panel">
  <h2>CLOUD POS SOFTWARE</h2>
  <div class="dots"><i></i><i></i><i></i></div>
  <p>Lorem Ipsum is simply dummy text of the printing and typesetting industry. Lorem Ipsum has been the industry's standard dummy text ever since the 1500s, when an unknown printer took a galley of type and scrambled it to make a type specimen book. It has survived not only five centuries. Lorem Ipsum is simply dummy text of the printing and typesetting industry. Lorem Ipsum has been the industry's standard dummy text ever since the 1500s, Lorem Ipsum has been the industry's standard dummy text ever since the 1500s,</p>
  <p>Lorem Ipsum is simply dummy text of the printing and typesetting industry. Lorem Ipsum has been the industry's standard dummy text ever since the 1500s, when an unknown printer took a galley of type and scrambled it to make a type specimen book. It has survived not only five centuries. Lorem Ipsum is simply dummy text of the printing and typesetting industry.</p>
  <div class="btn-outline">READ MORE
    <svg width="12" height="12" viewBox="0 0 12 12"><circle cx="6" cy="6" r="6" fill="#1b1b1b"/><path d="M5 3.5L7.5 6 5 8.5" fill="none" stroke="#f1c40f" stroke-width="1.5"/></svg>
  </div>
</section>

<section class="pos">
  <h2 class="pos-title">POS</h2>
  <p class="pos-sub">Thousands of free features without having to download any 3rd party apps</p>
  <svg class="orbit" width="1200" height="857">
    <circle cx="600" cy="518" r="283" fill="none" stroke="#666" stroke-width="1.2" stroke-dasharray="2 4"/>
    <circle cx="600" cy="518" r="267" fill="none" stroke="#999" stroke-width="1" stroke-dasharray="2 5"/>
  </svg>
  <div class="hardware" role="img" aria-label="POS hardware set: touchscreen terminal, receipt printer, cash drawer and scanner"></div>

  <div class="feature" style="left:543px;top:186px">
    <svg width="56" height="56" viewBox="0 0 56 56" fill="none" stroke="#1b1b1b" stroke-width="2"><rect x="6" y="8" width="44" height="30" rx="2"/><path d="M22 46h12M28 38v8M12 16h12M12 22h10M12 28h12"/><path d="M30 30l5-7 4 4 6-10"/></svg>
  </div>
  <div class="feature-label" style="left:535px;top:303px">Virtual Dashboards</div>

  <div class="feature" style="left:277px;top:387px">
    <svg width="56" height="56" viewBox="0 0 56 56" fill="none" stroke="#1b1b1b" stroke-width="2"><rect x="14" y="6" width="24" height="42" rx="3"/><path d="M23 42h6M20 24l5 5 10-10"/></svg>
  </div>
  <div class="feature-label" style="left:238px;top:488px">Mobile</div>

  <div class="feature" style="left:790px;top:373px">
    <svg width="56" height="56" viewBox="0 0 56 56" fill="none" stroke="#1b1b1b" stroke-width="2"><path d="M6 12h6l6 24h24l4-16"/><circle cx="22" cy="44" r="3"/><circle cx="38" cy="44" r="3"/><circle cx="31" cy="20" r="9"/><path d="M22 20h18M31 11v18"/></svg>
  </div>
  <div class="feature-label" style="left:892px;top:470px">eCommerce</div>

  <div class="feature" style="left:367px;top:670px">
    <svg width="56" height="56" viewBox="0 0 56 56" fill="none" stroke="#1b1b1b" stroke-width="2"><rect x="8" y="14" width="22" height="18"/><path d="M19 32v14M12 46h14"/><circle cx="40" cy="14" r="5"/><path d="M34 46V26h12v20"/></svg>
  </div>
  <div class="feature-label" style="left:321px;top:747px">Kiosks</div>

  <div class="feature" style="left:720px;top:663px">
    <svg width="56" height="56" viewBox="0 0 56 56" fill="none" stroke="#1b1b1b" stroke-width="2"><rect x="10" y="8" width="30" height="22" rx="2"/><rect x="16" y="14" width="18" height="10"/><path d="M6 40h44v8H6zM25 30v10"/></svg>
  </div>
  <div class="feature-label" style="left:829px;top:746px">Ecosystem</div>
</section>

<section class="banner">
  <div class="brand"><span class="mark"></span>RK Till Depot</div>
  <div class="divider"></div>
  <h3>BETTER SOFTWARE FOR A BETTER BUSINESS</h3>
  <p>The only software you need, Moving your business forward</p>
  <div class="btn-banner">
    <svg width="13" height="10" viewBox="0 0 13 10"><rect x=".7" y=".7" width="11.6" height="8.6" fill="none" stroke="#fff" stroke-width="1.3"/><path d="M.7 .7l5.8 4.5 5.8-4.5" fill="none" stroke="#fff" stroke-width="1.3"/></svg>CONTACT US
  </div>
</section>

<h2 class="smart-title">A SMART POS SOLUTION TAILOR</h2>
<p class="smart-sub">Made for Your Business</p>

<div class="hex" style="left:134px;top:2749px">
  <svg width="70" height="60" viewBox="0 0 70 60" fill="none" stroke="#1b1b1b" stroke-width="2.5"><path d="M4 6h9l8 32h36l6-22H17"/><circle cx="26" cy="50" r="4"/><circle cx="50" cy="50" r="4"/><path d="M30 14v16M42 14v16"/></svg>Book Store</div>
<div class="hex" style="left:400px;top:2749px">
  <svg width="70" height="60" viewBox="0 0 70 60" fill="none" stroke="#1b1b1b" stroke-width="2.5"><rect x="6" y="14" width="58" height="40" rx="4"/><path d="M26 14V6h18v8M35 24v20M25 34h20"/></svg>Health Store</div>
<div class="hex" style="left:632px;top:2749px">
  <svg width="70" height="60" viewBox="0 0 70 60" fill="none" stroke="#1b1b1b" stroke-width="2.5"><path d="M10 24h42v8a20 20 0 0 1-42 0z"/><path d="M52 28h6a6 6 0 0 1 0 12h-8M6 56h56M24 4c4 5-4 8 0 14M34 4c4 5-4 8 0 14"/></svg>Coffee Shop</div>
<div class="hex" style="left:854px;top:2749px">
  <svg width="70" height="60" viewBox="0 0 70 60" fill="none" stroke="#1b1b1b" stroke-width="2.5"><rect x="8" y="18" width="54" height="12"/><rect x="12" y="30" width="46" height="26"/><path d="M35 18v38M35 18c-6-12-18-10-14-2M35 18c6-12 18-10 14-2"/></svg>Gift Shop</div>
<div class="hex" style="left:288px;top:2929px">
  <svg width="70" height="60" viewBox="0 0 70 60" fill="none" stroke="#1b1b1b" stroke-width="2.5"><path d="M8 56h54M14 56V30h12v26M26 56V14h18v42M44 56V30h12v26M32 22h6M32 32h6M32 42h6"/></svg>Multi Store</div>
<div class="hex" style="left:520px;top:2929px">
  <svg width="70" height="60" viewBox="0 0 70 60" fill="none" stroke="#1b1b1b" stroke-width="2.5"><path d="M6 18h58l-4-12H10zM10 18v38h50V18M18 56V30h14v26M40 30h12v12H40z"/></svg>Hardware Store</div>
<div class="hex" style="left:742px;top:2929px">
  <svg width="70" height="60" viewBox="0 0 70 60" fill="none" stroke="#1b1b1b" stroke-width="2.5"><path d="M6 22h58M10 22v34h50V22M10 36h50M30 36v20"/><path d="M32 18V4l12-2v14"/><circle cx="29" cy="18" r="3"/><circle cx="41" cy="16" r="3"/></svg>Music Store</div>

<h2 class="partners-title">OUR PARTNERS LOVE US:</h2>
<div class="arrow" style="left:102px"><svg width="10" height="10" viewBox="0 0 10 10" style="transform:rotate(-45deg)"><path d="M6.5 1.5L3 5l3.5 3.5" fill="none" stroke="#fff" stroke-width="1.8"/></svg></div>
<div class="partner" style="left:160px"><i></i>Ember Lane</div>
<div class="partner" style="left:340px"><i></i>Cloudmint</div>
<div class="partner" style="left:519px"><i></i>Vantor Labs</div>
<div class="partner" style="left:698px"><i></i>Talkbay</div>
<div class="partner" style="left:876px"><i></i>Grainly</div>
<div class="arrow" style="left:1066px"><svg width="10" height="10" viewBox="0 0 10 10" style="transform:rotate(-45deg)"><path d="M3.5 1.5L7 5 3.5 8.5" fill="none" stroke="#fff" stroke-width="1.8"/></svg></div>

<footer class="site-footer">
  <div class="foot-col" style="left:150px"><h4>FEATURES</h4><ul><li>POINT OF SALE</li><li>STORE MANAGEMENT</li><li>MENUS &amp; MODIFIERS</li><li>CHECKOUT</li><li>CUSTOMER LOYALTY</li><li>REPORTING</li></ul></div>
  <div class="foot-col" style="left:358px"><h4>BUSINESS TYPES</h4><ul><li>RETAIL</li><li>FOOD &amp; BEVERAGE</li><li>HEALTH &amp; BEAUTY</li><li>ENTERTAINMENT</li><li>OTHER BUSINESSES</li></ul></div>
  <div class="foot-col" style="left:563px"><h4>BECOME A PARTNER</h4><ul><li>WHY PARTNER WITH</li><li>OUR PROMISE</li><li>LOGIN</li><li>REGISTRATION</li></ul></div>
  <div class="foot-col" style="left:781px"><h4 style="width:245px">SIGN UP FOR NEWSLETTER</h4></div>
  <div class="news-input" style="left:782px;top:90px">Enter your name</div>
  <div class="news-input" style="left:782px;top:158px">Enter your email</div>
  <div class="btn-subscribe">SUBSCRIBE</div>
</footer>

<div class="copyright">
  <span>© 2021 rtilsystem.com. All Rights Reserved.</span>
  <div class="social"><i></i><i></i><i></i><i></i><i></i></div>
</div>

</body>
</html>
```